Fernbrook Pet Showcase Ticket Card Design

We’re looking to create a complimentary “ticket” card for Fernbrook Pet Showcase that can be handed out physically. We host an event for cat lovers. The card should feel special and collectible. Size will be a standard business card (3.5" x 2") Orientation is open to designer recommendation. This ticket will be used as a complimentary entry pass for select guests, partners, & giveaways. Key elements to Include are the Fernbrook Pet Showcase logo (provided), the words “Complimentary Ticket” or similar wording (open to creative phrasing and cat puns) A blank space for the Event date (to be written in) & Ticket number (to be written in) . Event Name is always "Fernbrook Pet Bazaar & Rehoming Day". We want the ticket to feel clean & modern but slightly playful with a cat-inspired touch (think clever, not kitschy). Could include a subtle cat motif or texture (e.g., whisker lines, paw detail, soft patterning) Open to unique layout ideas that still leave clear writing space. Avoid overcrowding of elements. Ticket should also have fine print "This ticket is not redeemable for cash and cannot be combined with any other offers or discounts, can only be used for the date indicated"

Target Market(s)

Women

Industry/Entity Type

pets

Colors
6B429C
8869AF
B7A5CE
E3DAEB
F3F0F8

Requirements
Must have
• Fernbrook Pet Showcase Logo & words around complimentary ticket as well as the fine print
Nice to have
• cat-inspired touch (think clever, not kitschy). Could include a subtle cat motif or texture (e.g., whisker lines, paw detail, soft patterning)
Should not have
• should not look cartoony

```html
<!DOCTYPE html>
<html lang="en">
<head>
<meta charset="utf-8">
<title>Fernbrook Pet Showcase – Complimentary Ticket Options</title>
<link rel="stylesheet" href="https://fonts.googleapis.com/css2?family=Oswald:wght@300;400;500;600&family=Montserrat:wght@400&display=swap">
<style>
  :root {
    --page-bg: #cccccc;
    --card-bg: #000000;
    --paper: #ffffff;
    --field-bg: #e6e6e6;
    --field-ink: #222222;
    --label-ink: #111111;
    --fine-ink: #bdbdbd;
  }
  html, body {
    margin: 0;
    padding: 0;
    width: 1200px;
    height: 2234px;
    overflow: hidden;
    background: var(--page-bg);
  }
  .sheet {
    position: relative;
    width: 1200px;
    height: 2234px;
  }
  .option-label {
    position: absolute;
    left: 0;
    width: 1200px;
    margin: 0;
    text-align: center;
    font-family: "Montserrat", sans-serif;
    font-weight: 400;
    font-size: 25px;
    letter-spacing: 36px;
    text-indent: 36px;
    color: var(--label-ink);
    line-height: 1;
  }
  .ticket {
    position: absolute;
    left: 129px;
    width: 941px;
    height: 553px;
    background: var(--card-bg);
    overflow: hidden;
    box-shadow: 0 26px 20px -14px rgba(0,0,0,.38);
  }
  .ticket--pink     { --accent: #f28cb8; --accent-dim: #8a4f66; --paw: #5a3340; }
  .ticket--violet   { --accent: #8657d0; --accent-dim: #4b2e72; --paw: #4b2e72; }
  .ticket--lavender { --accent: #dca0f0; --accent-dim: #7a5a8a; --paw: #7a5a8a; }

  .ticket__art {
    position: absolute;
    inset: 0;
    width: 941px;
    height: 553px;
  }
  .ticket__headline {
    position: absolute;
    right: 424px;
    top: 28px;
    margin: 0;
    text-align: right;
    font-family: "Oswald", sans-serif;
    line-height: 1;
  }
  .ticket__kicker {
    display: block;
    font-weight: 500;
    font-size: 60px;
    letter-spacing: -1px;
    color: var(--paper);
    transform: scaleX(.88);
    transform-origin: right;
  }
  .ticket__word {
    display: block;
    margin-top: -14px;
    font-weight: 500;
    font-size: 140px;
    letter-spacing: -2px;
    color: var(--accent);
    transform: scaleX(.93);
    transform-origin: right;
  }
  .ticket__event {
    position: absolute;
    left: 60px;
    width: 540px;
    top: 270px;
    margin: 0;
    text-align: center;
    font-family: "Oswald", sans-serif;
    font-weight: 400;
    font-size: 64px;
    line-height: 70px;
    color: var(--paper);
    letter-spacing: -.5px;
  }
  .ticket__fields {
    position: absolute;
    left: 33px;
    top: 451px;
    width: 646px;
    height: 65px;
    border-radius: 20px;
    background: var(--field-bg);
    font-family: "Oswald", sans-serif;
    font-weight: 300;
    font-size: 26px;
    color: var(--field-ink);
  }
  .field {
    position: absolute;
    top: 18px;
    display: flex;
    align-items: flex-end;
    gap: 12px;
    line-height: 1;
  }
  .field__line {
    display: block;
    height: 0;
    border-bottom: 1.5px dotted #666;
    margin-bottom: 2px;
  }
  .field--date { left: 22px; }
  .field--date .field__line { width: 268px; }
  .field--number { left: 369px; }
  .field--number .field__line { width: 158px; }
  .ticket__fine-print {
    position: absolute;
    left: 33px;
    top: 523px;
    width: 646px;
    margin: 0;
    font-family: "Oswald", sans-serif;
    font-weight: 300;
    font-size: 10.5px;
    line-height: 13px;
    color: var(--fine-ink);
    text-align: center;
  }
  .ticket__brand {
    position: absolute;
    left: 620px;
    top: 72px;
    width: 262px;
    margin: 0;
    text-align: center;
    font-family: "Oswald", sans-serif;
    font-weight: 600;
    font-size: 48px;
    line-height: 56px;
    color: #000000;
  }
</style>
</head>
<body>
<main class="sheet">

  <p class="option-label" style="top:80px">OPTION 1</p>
  <article class="ticket ticket--pink" style="top:147px">
    <svg class="ticket__art" viewBox="0 0 941 553">
      <rect x="0" y="0" width="180" height="118" rx="28" fill="var(--accent-dim)" role="img" aria-label="Cat toy illustration"/>
      <rect x="14" y="128" width="95" height="95" rx="40" fill="var(--paw)" role="img" aria-label="Paw print motif"/>
      <rect x="642" y="308" width="91" height="91" rx="38" fill="var(--paw)" role="img" aria-label="Paw print motif"/>
      <circle cx="772" cy="100" r="232" fill="var(--paper)"/>
      <circle cx="772" cy="100" r="210" fill="none" stroke="var(--accent)" stroke-width="5"/>
      <path d="M694 553 C730 525 770 528 800 505 C835 480 840 440 880 418 C905 405 930 395 941 372 L941 553 Z" fill="var(--accent)"/>
      <rect x="751" y="334" width="156" height="173" rx="60" fill="var(--accent-dim)" role="img" aria-label="Cat silhouette illustration"/>
    </svg>
    <p class="ticket__brand">Fernbrook<br>Pet Showcase</p>
    <h2 class="ticket__headline"><span class="ticket__kicker">COMPLIMENTARY</span><span class="ticket__word">TICKET</span></h2>
    <p class="ticket__event">Fernbrook Pet Bazaar<br>&amp; Rehoming Day</p>
    <div class="ticket__fields">
      <span class="field field--date">Date :<span class="field__line"></span></span>
      <span class="field field--number">Ticket no.<span class="field__line"></span></span>
    </div>
    <p class="ticket__fine-print">This ticket is not redeemable for cash and cannot be combined with any other offers or discounts, can only be used for the date indicated</p>
  </article>

  <p class="option-label" style="top:795px">OPTION 2</p>
  <article class="ticket ticket--violet" style="top:854px">
    <svg class="ticket__art" viewBox="0 0 941 553">
      <rect x="0" y="0" width="180" height="118" rx="28" fill="var(--accent-dim)" role="img" aria-label="Cat toy illustration"/>
      <rect x="14" y="128" width="95" height="95" rx="40" fill="var(--paw)" role="img" aria-label="Paw print motif"/>
      <rect x="642" y="308" width="91" height="91" rx="38" fill="var(--paw)" role="img" aria-label="Paw print motif"/>
      <circle cx="772" cy="100" r="232" fill="var(--paper)"/>
      <circle cx="772" cy="100" r="210" fill="none" stroke="var(--accent)" stroke-width="5"/>
      <path d="M694 553 C730 525 770 528 800 505 C835 480 840 440 880 418 C905 405 930 395 941 372 L941 553 Z" fill="var(--accent)"/>
      <rect x="751" y="334" width="156" height="173" rx="60" fill="var(--accent-dim)" role="img" aria-label="Cat silhouette illustration"/>
    </svg>
    <p class="ticket__brand">Fernbrook<br>Pet Showcase</p>
    <h2 class="ticket__headline"><span class="ticket__kicker">COMPLIMENTARY</span><span class="ticket__word">TICKET</span></h2>
    <p class="ticket__event">Fernbrook Pet Bazaar<br>&amp; Rehoming Day</p>
    <div class="ticket__fields">
      <span class="field field--date">Date :<span class="field__line"></span></span>
      <span class="field field--number">Ticket no.<span class="field__line"></span></span>
    </div>
    <p class="ticket__fine-print">This ticket is not redeemable for cash and cannot be combined with any other offers or discounts, can only be used for the date indicated</p>
  </article>

  <p class="option-label" style="top:1502px">OPTION 3</p>
  <article class="ticket ticket--lavender" style="top:1574px">
    <svg class="ticket__art" viewBox="0 0 941 553">
      <rect x="0" y="0" width="180" height="118" rx="28" fill="var(--accent-dim)" role="img" aria-label="Cat toy illustration"/>
      <rect x="14" y="128" width="95" height="95" rx="40" fill="var(--paw)" role="img" aria-label="Paw print motif"/>
      <rect x="642" y="308" width="91" height="91" rx="38" fill="var(--paw)" role="img" aria-label="Paw print motif"/>
      <circle cx="772" cy="100" r="232" fill="var(--paper)"/>
      <circle cx="772" cy="100" r="210" fill="none" stroke="var(--accent)" stroke-width="5"/>
      <path d="M694 553 C730 525 770 528 800 505 C835 480 840 440 880 418 C905 405 930 395 941 372 L941 553 Z" fill="var(--accent)"/>
      <rect x="751" y="334" width="156" height="173" rx="60" fill="var(--accent-dim)" role="img" aria-label="Cat silhouette illustration"/>
    </svg>
    <p class="ticket__brand">Fernbrook<br>Pet Showcase</p>
    <h2 class="ticket__headline"><span class="ticket__kicker">COMPLIMENTARY</span><span class="ticket__word">TICKET</span></h2>
    <p class="ticket__event">Fernbrook Pet Bazaar<br>&amp; Rehoming Day</p>
    <div class="ticket__fields">
      <span class="field field--date">Date :<span class="field__line"></span></span>
      <span class="field field--number">Ticket no.<span class="field__line"></span></span>
    </div>
    <p class="ticket__fine-print">This ticket is not redeemable for cash and cannot be combined with any other offers or discounts, can only be used for the date indicated</p>
  </article>

</main>
</body>
</html>
```